Business Card Design

Maple Crest Rentals
Maple Crest Rentals is a high end home rental leasing company that provides exquisite properties in niche markets. We are a small family owned business that considers our clients not as renters, but as friends. Every property we buy must be brought up to our high standards before it is offered on the market. The properties that we lease are exceptional, "move in" ready homes. This allows for the client to take pride in their lease as if it was their own home. To put it another way; we do not lease a property that we would not live in ourselves.

Target Market(s)

Couples making $100K or more

Industry/Entity Type

Business

Requirements
Must have
• Some sort of logo
Nice to have
• good slogan
Should not have
• Pink

```html
<!DOCTYPE html>
<html lang="en">
<head>
<meta charset="utf-8">
<title>Maple Crest Rentals – Business Card</title>
<link href="https://fonts.googleapis.com/css2?family=Crimson+Pro:wght@700&display=swap" rel="stylesheet">
<style>
  :root {
    --card-bg: #edf0dc;
    --forest: #1c4a0b;
    --bark: #392a07;
    --cream: #f7f2df;
  }
  html, body {
    margin: 0;
    padding: 0;
    overflow: hidden;
    background: var(--card-bg);
  }
  .card {
    position: relative;
    width: 704px;
    height: 1200px;
    background: var(--card-bg);
    font-family: "Crimson Pro", Georgia, serif;
    font-weight: 700;
    overflow: hidden;
  }
  .brand-mark {
    position: absolute;
    left: 277px;
    top: 130px;
    width: 150px;
    height: 150px;
    border-radius: 50%;
    background: var(--forest);
  }
  .brand-name {
    position: absolute;
    left: 0;
    top: 318px;
    width: 704px;
    margin: 0;
    text-align: center;
    color: var(--forest);
    font-size: 70px;
    line-height: 1;
    letter-spacing: 1px;
    text-transform: uppercase;
  }
  .slogan {
    position: absolute;
    left: 0;
    top: 566px;
    width: 704px;
    margin: 0;
    text-align: center;
    color: var(--forest);
    font-size: 31px;
    letter-spacing: 7px;
    line-height: 1;
  }
  .contact-panel {
    position: absolute;
    left: 112px;
    top: 642px;
    width: 479px;
    height: 439px;
    background: var(--bark);
    color: var(--cream);
    text-align: center;
    font-size: 29px;
    line-height: 1;
  }
  .contact-panel p {
    position: absolute;
    left: 0;
    width: 100%;
    margin: 0;
  }
  .promise-band {
    position: absolute;
    left: 31px;
    top: 1083px;
    width: 642px;
    height: 57px;
    background: var(--forest);
    color: var(--cream);
    font-size: 31px;
    line-height: 57px;
    text-align: center;
    margin: 0;
  }
</style>
</head>
<body>
  <div class="card">
    <div class="brand-mark" aria-hidden="true"></div>
    <h1 class="brand-name">Maple Crest<br>Rentals</h1>
    <p class="slogan">HOME SWEET HOME</p>

    <div class="contact-panel">
      <p style="top:24px">Name | Designation</p>
      <p style="top:81px">Mobile Number</p>
      <p style="top:185px">Address line 1</p>
      <p style="top:234px">Address line 2 Address line 2</p>
      <p style="top:284px">Address line 3 Address line 3</p>
      <p style="top:333px">Email Address</p>
      <p style="top:382px">Website address</p>
    </div>

    <p class="promise-band">High Standard "move In" Ready Homes</p>
  </div>
</body>
</html>
```